WE ARE REACHING OUT TO CONTRACTORS TO HAVE AN OPPORTUNITY TO PROVIDE PROPOSALS FOR THEIR PROJECTS.

WE ARE A WASHINGTON DC. METRO AREA PLUMBING, HEATING AND AIR CONDITIONING CONTRACTOR. WE WOULD LIKE TO PRESENT A POSTCARD THAT OFFERS A FRENDLY, CONVENIENT WAY TO PROVIDE PROPOSALS FOR THEIR UP COMMING PROJECTS. WE WOULD APPRECIATE THE OPPURTUNITY TO PROVIDE ESTIMATES FOR YOUR UP COMMING PROJECTS. IF REQUESTED, WE WILL PROVIDE SAME DAY WALK THRU'S AND PROPOSALS. GET A 2ND OPINION, WE ALL LOOK AT PROJECTS DIFFERENTLY. CUSTOM HOMES, SUB DIVISIONS, REMODELING, SEWER AND WATER INSTALLATIONS AND REPLACEMENTS, WELL AND SEPTIC INSTALLATIONS AND REPAIRS, MECHANICAL EQUIPTMENT CHANGE OUTS, PLUMBING SYSTEMS REPLACEMENTS AND REPAIRS. RESIDENTAL AND COMERICAL CONSTRUCTION.. " WE DO IT ALL" JUST GIVE US A CALL. " WE WILL BE THERE " I WOULD LIKE MY BUSINESS CARD ON THE FRONT WITH SOME MODIFICATIONS AND THE ABOVE DESCRIPTION ON THE BACK. " HIGHLIGHTING WE WOULD APPRICATE THE OPPORTUNITY TO WORK WITH YOU COMPANY " SAME DAY WALK THRU'S AND PROPOSALS. PLEASE ADDRESS THE TOP OF THE BACK IN BOLD PRINT. " ATTENTION ESTIMATING " EYE CATCHING COLORS PLEASE. THANK YOU, TOM SELWYN

```html
<!DOCTYPE html>
<html lang="en">
<head>
<meta charset="utf-8">
<title>T.M.Selwyn Mechanical Services – Contractor Postcard</title>
<link rel="stylesheet" href="https://fonts.googleapis.com/css2?family=Michroma&display=swap">
<style>
  :root {
    --backdrop: #2b2b2b;
    --card: #ffffff;
    --ink: #161616;
    --accent: #e02424;
    --rule: #9a9a9a;
    --font-main: "Michroma", sans-serif;
  }
  * { margin: 0; padding: 0; box-sizing: border-box; }
  html, body {
    width: 1200px;
    height: 751px;
    overflow: hidden;
    background: var(--backdrop);
    font-family: var(--font-main);
  }
  .canvas { position: relative; width: 1200px; height: 751px; }

  .postcard {
    position: absolute;
    background: var(--card);
    color: var(--ink);
    white-space: nowrap;
  }
  .postcard > * { position: absolute; }

  /* Front */
  .postcard--front { left: 21px; top: 21px; width: 550px; height: 353px; }
  .brand-name { left: 14px; top: 36px; font-size: 21px; font-weight: 400; letter-spacing: 0.5px; }
  .brand-tagline { left: 14px; top: 64px; font-size: 11px; color: var(--accent); }
  .brand-wordmark { left: 420px; top: 44px; font-size: 19px; color: var(--accent); }
  .slogan {
    left: 0; width: 100%; text-align: center;
    color: var(--accent);
  }
  .slogan--main { top: 157px; font-size: 13.5px; }
  .slogan--sub { top: 180px; font-size: 13.5px; }
  .front-rule { left: 10px; top: 258px; width: 535px; height: 3px; background: var(--ink); }
  .experience { left: 27px; top: 279px; font-size: 9px; }
  .services { left: 43px; top: 312px; font-size: 11px; color: var(--accent); word-spacing: 2px; }

  /* Back */
  .postcard--back { left: 588px; top: 317px; width: 593px; height: 362px; }
  .return-address { left: 15px; top: 18px; font-size: 11px; line-height: 19px; font-style: normal; }
  .stamp-box { left: 516px; top: 31px; width: 55px; height: 67px; border: 2px dashed var(--ink); }
  .divider { left: 374px; top: 74px; width: 1px; height: 240px; background: var(--ink); }
  .address-lines { left: 398px; top: 159px; width: 163px; height: 110px; }

  .message { left: 0; width: 374px; text-align: center; }
  .attention { top: 82px; font-size: 14px; font-weight: 700; letter-spacing: 0.5px; color: var(--ink); }
  .walkthru { top: 112px; font-size: 9.5px; color: var(--accent); }
  .appeal { color: var(--accent); }
  .appeal--lead { top: 150px; font-size: 14px; }
  .appeal--body { top: 174px; font-size: 11.5px; line-height: 18px; }
  .service-list {
    top: 226px; font-size: 6.8px; line-height: 12.5px;
    list-style: none; color: var(--ink);
  }

  .contact { top: 341px; font-size: 8.5px; }
  .contact--phone { left: 15px; }
  .contact--email { left: 216px; }
</style>
</head>
<body>
<main class="canvas">

  <section class="postcard postcard--front" aria-label="Postcard front">
    <h1 class="brand-name">T.M.SELWYN</h1>
    <p class="brand-tagline">MECHANICAL SERVICES</p>
    <p class="brand-wordmark">SELWYN</p>
    <p class="slogan slogan--main">" WE DO IT ALL" JUST GIVE US A CALL.</p>
    <p class="slogan slogan--sub">" WE WILL BE THERE "</p>
    <div class="front-rule"></div>
    <p class="experience">36YEARS RESIDENTIAL AND COMMERCIAL CONSTRUCTION AND REMODELING</p>
    <p class="services">PLUMBING | HEATING | AIR CONDITIONING | GAS FITTING</p>
  </section>

  <section class="postcard postcard--back" aria-label="Postcard back">
    <address class="return-address">1870 HOLLOW OAK ROAD<br>WESTFIELD,MD 21090</address>
    <div class="stamp-box"></div>
    <div class="divider"></div>
    <svg class="address-lines" viewBox="0 0 163 110" width="163" height="110" aria-hidden="true">
      <g stroke="#9a9a9a" stroke-width="1">
        <line x1="0" y1="1" x2="163" y2="1"/>
        <line x1="0" y1="25" x2="163" y2="25"/>
        <line x1="0" y1="49" x2="163" y2="49"/>
        <line x1="0" y1="77" x2="163" y2="77"/>
        <line x1="0" y1="103" x2="163" y2="103"/>
      </g>
    </svg>

    <h2 class="message attention">ATTENTION ESTIMATING</h2>
    <p class="message walkthru">SAME DAY WALK THRU'S AND PROPOSALS</p>
    <p class="message appeal appeal--lead">WE WOULD APPRECIATE THE</p>
    <p class="message appeal appeal--body">THE OPPORTUNITY TO WORK WITH YOU<br>COMPANY</p>
    <ul class="message service-list">
      <li>CUSTOM HOMES | SUB DIVISIONS | REMODELING</li>
      <li>SEWER AND WATER INSTALLATIONS AND REPLACEMENTS</li>
      <li>WELL AND SEPTIC INSTALLATIONS AND REPAIRS</li>
      <li>MECHANICAL EQUIPMENT CHANGE OUTS</li>
      <li>PLUMBING SYSTEMS REPLACEMENTS AND REPAIRS</li>
      <li>GET A 2ND OPINION, WE ALL LOOK AT PROJECTS DIFFERENTLY</li>
    </ul>

    <p class="contact contact--phone">301-555-0147</p>
    <p class="contact contact--email">TOMSELWYN@MAILBOX.COM</p>
  </section>

</main>
</body>
</html>
```